Business Cards for a Telecom Company
Harbor Signal
Business Cards for a Telecom Company - Telecommunications
Creative Brief
Professional
Mark Pelham
Employee
27 Birchwood Lane Suite 415 Brookhaven, CT 06410
mark@harborsignal.example
www.harborsignal.example
Harbor Signal inc www.facebook.com/Harborsignal www.twitter.com/Harborsignal Bringing the Could Revolution to your Home and Business
raymitchell27 raymitchell27
On the back if the Card please change " Bringing the Could Revolution to your Home and Business" to "We bring Global Cloud Communications to your Home and Business"

```html
<!DOCTYPE html>
<html lang="en">
<head>
<meta charset="utf-8">
<title>Harbor Signal – Business Card</title>
<link href="https://fonts.googleapis.com/css2?family=Open+Sans:wght@400;600;700&display=swap" rel="stylesheet">
<style>
  :root {
    --page-bg: #e9e6e2;
    --card-white: #ffffff;
    --brand-teal: #1b5875;
    --brand-teal-dark: #14465e;
    --ink-white: #ffffff;
  }
  * { box-sizing: border-box; margin: 0; padding: 0; }
  html, body { width: 1200px; height: 900px; overflow: hidden; }
  body {
    background: var(--page-bg);
    font-family: "Open Sans", Arial, sans-serif;
    display: flex; align-items: center; justify-content: center;
  }
  .business-card {
    position: relative;
    width: 900px; height: 514px;
    background: var(--card-white);
    box-shadow: 0 10px 30px rgba(0,0,0,0.18);
    overflow: hidden;
  }
  .card-waves { position: absolute; inset: 0; width: 100%; height: 100%; }
  .brand {
    position: absolute; left: 64px; top: 78px;
    display: flex; align-items: center; gap: 16px;
  }
  .brand-dot {
    width: 64px; height: 64px; border-radius: 50%;
    background: var(--brand-teal);
  }
  .brand-name {
    font-weight: 700; font-size: 44px; letter-spacing: 1px;
    color: var(--brand-teal); text-transform: uppercase;
  }
  .contact-list {
    position: absolute; left: 52px; top: 336px;
    list-style: none; color: var(--ink-white);
    font-size: 17px; line-height: 1.3;
  }
  .contact-item { display: flex; align-items: flex-start; gap: 10px; margin-bottom: 6px; }
  .contact-item.address { margin-bottom: 16px; }
  .contact-icon { width: 20px; height: 20px; flex: none; margin-top: 1px; }
  .person {
    position: absolute; right: 58px; top: 330px;
    text-align: right; color: var(--ink-white);
  }
  .person-name { font-weight: 700; font-size: 30px; line-height: 1.2; }
  .person-title { font-weight: 400; font-size: 25px; line-height: 1.5; }
</style>
</head>
<body>
  <div class="business-card">
    <svg class="card-waves" viewBox="0 0 900 514" aria-hidden="true">
      <defs>
        <linearGradient id="swooshGrey" x1="0" y1="0" x2="1" y2="0">
          <stop offset="0" stop-color="#eef0f1"/>
          <stop offset="0.55" stop-color="#c3c8cc"/>
          <stop offset="1" stop-color="#8e959b"/>
        </linearGradient>
        <linearGradient id="tealBand" x1="0" y1="0" x2="0" y2="1">
          <stop offset="0" stop-color="#1f6483"/>
          <stop offset="1" stop-color="#154a63"/>
        </linearGradient>
      </defs>
      <path d="M0 258 C 240 205, 470 300, 900 142 L900 178 C 520 318, 250 232, 0 284 Z" fill="url(#swooshGrey)"/>
      <path d="M0 240 C 250 190, 480 285, 900 128" fill="none" stroke="#d4d8db" stroke-width="3"/>
      <path d="M0 290 C 250 236, 510 318, 900 186 L900 514 L0 514 Z" fill="url(#tealBand)"/>
    </svg>

    <div class="brand">
      <span class="brand-dot"></span>
      <span class="brand-name">Harbor Signal</span>
    </div>

    <ul class="contact-list">
      <li class="contact-item address">
        <svg class="contact-icon" viewBox="0 0 20 20"><circle cx="10" cy="10" r="10" fill="#fff"/><path d="M10 4.5a3.5 3.5 0 0 0-3.5 3.5c0 2.6 3.5 7 3.5 7s3.5-4.4 3.5-7A3.5 3.5 0 0 0 10 4.5zm0 5a1.4 1.4 0 1 1 0-2.8 1.4 1.4 0 0 1 0 2.8z" fill="#1b5875"/></svg>
        <span>27 Birchwood Lane Suite 415<br>Brookhaven, CT 06410</span>
      </li>
      <li class="contact-item">
        <svg class="contact-icon" viewBox="0 0 20 20"><circle cx="10" cy="10" r="10" fill="#fff"/><path d="M7 5.2l1.6 2.4-1 1.1a7 7 0 0 0 3.7 3.7l1.1-1 2.4 1.6-.9 1.8c-4.6-.4-8.3-4.1-8.7-8.7z" fill="#1b5875"/></svg>
        <span>1-555-010-0142</span>
      </li>
      <li class="contact-item">
        <svg class="contact-icon" viewBox="0 0 20 20"><circle cx="10" cy="10" r="10" fill="#fff"/><rect x="5" y="6.5" width="10" height="7" rx="1" fill="#1b5875"/><path d="M5.3 7l4.7 3.6L14.7 7" fill="none" stroke="#fff" stroke-width="1"/></svg>
        <span>mark@harborsignal.example</span>
      </li>
      <li class="contact-item">
        <svg class="contact-icon" viewBox="0 0 20 20"><circle cx="10" cy="10" r="10" fill="#fff"/><circle cx="10" cy="10" r="5" fill="none" stroke="#1b5875" stroke-width="1.3"/><path d="M5 10h10M10 5c-2.5 3-2.5 7 0 10M10 5c2.5 3 2.5 7 0 10" fill="none" stroke="#1b5875" stroke-width="1"/></svg>
        <span>www.harborsignal.example</span>
      </li>
    </ul>

    <div class="person">
      <p class="person-name">Mark Pelham</p>
      <p class="person-title">Employee</p>
    </div>
  </div>
</body>
</html>
```